LTV Business Card

This is a wide-range political consulting firm specializing in high-profile political campaigns. Red should be a predominant color in the business card, since this is a Heartland Party inspired consulting firm, but the word "heartland" will not appear anywhere in any kind of literature. Look has to be clean and crisp. The design should be forward thinking and appropriate for a company that is trying to break away from a traditionally "stodgy" image in politics.

Target Market(s)

potential national political candidates, wealthy donors,

Industry/Entity Type

Political

Contact Information for Business Card

Lionel T. Vardmoor
Political Consultant
438 Ormond Lane NW
#356
Washington, DC 20471

```html
<!DOCTYPE html>
<html lang="en">
<head>
<meta charset="utf-8">
<title>LTV Business Card</title>
<link rel="stylesheet" href="https://fonts.googleapis.com/css2?family=Arimo:wght@400;700&family=Open+Sans:wght@400&display=swap">
<style>
  :root {
    --backdrop: #1f2d42;
    --card-red: #962630;
    --stripe-light: #a7262f;
    --stripe-dark: #7e2431;
    --ink-white: #ffffff;
    --dot-light: #f4f4f4;
  }
  html, body {
    margin: 0;
    width: 1200px;
    height: 970px;
    overflow: hidden;
    background: var(--backdrop);
  }
  .stage {
    position: relative;
    width: 1200px;
    height: 970px;
  }
  .card {
    position: absolute;
    width: 620px;
    height: 360px;
    background: var(--card-red);
    overflow: hidden;
    box-shadow: 0 10px 28px rgba(0,0,0,.45);
    font-family: "Arimo", Arial, sans-serif;
    color: var(--ink-white);
  }
  .card__stripes {
    position: absolute;
    top: 0; bottom: 0; left: 0;
    width: 330px;
    background: linear-gradient(90deg,
      var(--stripe-light) 0 40px,
      var(--stripe-dark) 40px 90px,
      var(--stripe-light) 90px 135px,
      var(--stripe-dark) 135px 180px,
      var(--stripe-light) 180px 225px,
      var(--stripe-dark) 225px 270px,
      var(--stripe-light) 270px 330px);
  }
  .card--stacked { left: 470px; top: 80px; }
  .card--inline { left: 110px; top: 530px; }

  .brand {
    position: absolute;
    display: flex;
    align-items: center;
    gap: 12px;
  }
  .brand__dot {
    width: 34px;
    height: 34px;
    border-radius: 50%;
    background: var(--dot-light);
  }
  .brand__name {
    font-family: "Arimo", Arial, sans-serif;
    font-weight: 700;
    font-size: 44px;
    line-height: 1;
    color: var(--ink-white);
    letter-spacing: 1px;
  }
  .card--stacked .brand { left: 105px; top: 155px; }
  .card--inline .brand { left: 80px; top: 155px; }

  .holder__name {
    margin: 0;
    font-weight: 700;
    font-size: 25px;
    letter-spacing: .5px;
    text-transform: uppercase;
    text-shadow: 1px 2px 3px rgba(0,0,0,.45);
    white-space: nowrap;
  }
  .holder__role {
    margin: 6px 0 0;
    font-family: "Open Sans", Arial, sans-serif;
    font-size: 12px;
    text-transform: uppercase;
    letter-spacing: .3px;
  }
  .address {
    margin: 0;
    font-style: normal;
    font-weight: 700;
    font-size: 17px;
    line-height: 1.35;
    text-transform: uppercase;
    text-shadow: 1px 2px 3px rgba(0,0,0,.45);
    white-space: nowrap;
  }

  .card--stacked .holder { position: absolute; right: 55px; top: 190px; text-align: right; }
  .card--stacked .address { position: absolute; right: 75px; top: 268px; text-align: center; }

  .card--inline .holder { position: absolute; right: 35px; top: 135px; text-align: right; }
  .card--inline .holder__name { font-size: 23px; }
  .card--inline .address { position: absolute; left: 100px; bottom: 52px; }
</style>
</head>
<body>
<main class="stage">
  <section class="card card--stacked" aria-label="Business card, stacked address style">
    <div class="card__stripes"></div>
    <div class="brand"><span class="brand__dot"></span><span class="brand__name">LTV</span></div>
    <div class="holder">
      <h1 class="holder__name">Lionel T. Vardmoor</h1>
      <p class="holder__role">Political Consultant</p>
    </div>
    <address class="address">438 Ormond Lane<br>NW #356 Washington,<br>DC 20471</address>
  </section>

  <section class="card card--inline" aria-label="Business card, single-line address style">
    <div class="card__stripes"></div>
    <div class="brand"><span class="brand__dot"></span><span class="brand__name">LTV</span></div>
    <div class="holder">
      <h2 class="holder__name">Lionel T. Vardmoor</h2>
      <p class="holder__role">Political Consultant</p>
    </div>
    <address class="address">438 Ormond Lane NW #356 Washington, DC 20471</address>
  </section>
</main>
</body>
</html>
```